TMC Feedback sticker

We need a sticker design for our secondary school (aged 11 - 18). This is to allow teachers to provide feedback to students and vice-versa, having a conversation with the learner. I would love to have at least two different designs and it to be attractive, so that all can be included. I've attached the basic outline with the information to be presented. It should be A5 size, so that 2 of these can be fitted in.

Target Market(s)

Secondary school students

Industry/Entity Type

School

Font styles to use
Sans Serif

Requirements
Must have
• Attached details of the headings and enough space for all parties to respond.
Should not have
• Anything deemed inappropriate for secondary students

```html
<!DOCTYPE html>
<html lang="en">
<head>
<meta charset="utf-8">
<title>Formative Feedback Sticker</title>
<link rel="stylesheet" href="https://fonts.googleapis.com/css2?family=Righteous&family=Bubblegum+Sans&family=Roboto+Condensed:wght@400&display=swap">
<style>
  :root {
    --green-dark: #1e6b2a;
    --green: #2c9a3a;
    --green-light: #5cb84a;
    --orange: #f07a22;
    --red: #d42a1e;
    --sand: #ece595;
    --yellow: #ffd200;
    --yellow-deep: #f2b400;
    --star-red: #ef4f23;
    --paper: #ffffff;
    --mark: #9a9a9a;
  }
  html, body { margin: 0; padding: 0; overflow: hidden; }
  body { width: 1200px; height: 875px; background: var(--paper); }
  .sticker { position: relative; width: 1200px; height: 875px; overflow: hidden; }
  .sticker__shapes { position: absolute; inset: 0; }
  .title {
    position: absolute; left: 108px; top: 78px; margin: 0;
    font-family: "Righteous", sans-serif; font-weight: 400;
    font-size: 49px; line-height: 42px; letter-spacing: 2px;
    color: var(--green-light); -webkit-text-stroke: 2px var(--green-dark);
  }
  .label {
    position: absolute; margin: 0;
    font-family: "Bubblegum Sans", sans-serif; font-size: 20px; line-height: 27px;
    color: var(--green);
  }
  .label--red { color: var(--red); }
  .label--date { left: 812px; top: 134px; font-size: 24px; }
  .date-year { position: absolute; left: 1004px; top: 134px; font-family: "Roboto Condensed", sans-serif; font-size: 24px; color: var(--green); }
  .label--strengths { left: 123px; top: 223px; }
  .label--target { left: 106px; top: 335px; }
  .label--action { left: 106px; top: 452px; font-family: "Righteous", sans-serif; font-size: 22px; }
  .label--student { left: 108px; top: 572px; }
  .label--teacher { left: 628px; top: 572px; }
</style>
</head>
<body>
<div class="sticker">
  <svg class="sticker__shapes" width="1200" height="875" viewBox="0 0 1200 875" aria-hidden="true">
    <!-- trim marks -->
    <g stroke="var(--mark)" stroke-width="1">
      <line x1="62" y1="0" x2="62" y2="48"/><line x1="0" y1="58" x2="50" y2="58"/>
      <line x1="1138" y1="0" x2="1138" y2="48"/><line x1="1150" y1="58" x2="1200" y2="58"/>
      <line x1="62" y1="827" x2="62" y2="875"/><line x1="0" y1="817" x2="50" y2="817"/>
      <line x1="1138" y1="827" x2="1138" y2="875"/><line x1="1150" y1="817" x2="1200" y2="817"/>
    </g>
    <!-- outer frame -->
    <rect class="frame" x="81" y="72" width="1046" height="732" fill="none" stroke="var(--orange)" stroke-width="4"/>
    <rect x="84" y="75" width="1040" height="726" fill="none" stroke="var(--orange)" stroke-width="1.2" opacity=".6"/>
    <!-- title rules -->
    <line x1="757" y1="82" x2="757" y2="212" stroke="var(--green)" stroke-width="1.5"/>
    <line x1="92" y1="216" x2="768" y2="216" stroke="var(--green)" stroke-width="1.5"/>
    <!-- date line -->
    <line x1="880" y1="162" x2="1082" y2="162" stroke="var(--green)" stroke-width="1.5"/>
    <!-- ticks -->
    <g fill="none" stroke="var(--green)" stroke-width="3" stroke-linecap="round">
      <path d="M130 266 l8 9 l18 -22"/>
      <path d="M130 299 l8 9 l18 -22"/>
    </g>
    <!-- target & action panels -->
    <rect x="90" y="328" width="1017" height="112" rx="32" fill="var(--sand)" stroke="var(--green-dark)" stroke-width="2"/>
    <rect x="93" y="447" width="1017" height="113" rx="32" fill="var(--sand)" stroke="var(--green-dark)" stroke-width="2"/>
    <!-- student panel -->
    <rect x="96" y="569" width="492" height="223" fill="var(--sand)" stroke="var(--yellow-deep)" stroke-width="3"/>
    <g stroke="var(--paper)" stroke-width="2.5">
      <line x1="105" y1="647" x2="578" y2="647"/>
      <line x1="105" y1="676" x2="578" y2="676"/>
      <line x1="105" y1="705" x2="578" y2="705"/>
      <line x1="105" y1="740" x2="578" y2="740"/>
      <line x1="105" y1="772" x2="578" y2="772"/>
    </g>
    <!-- pen icon -->
    <g fill="none" stroke="var(--green-dark)" stroke-width="2.5" stroke-linejoin="round">
      <path d="M518 623 l8 -20 l44 -26 q10 -4 12 5 q1 6 -6 10 l-44 26 z"/>
      <path d="M526 603 l12 12"/>
      <path d="M556 585 l8 12"/>
    </g>
    <!-- teacher panel -->
    <rect x="619" y="569" width="492" height="223" fill="var(--paper)" stroke="var(--yellow)" stroke-width="3"/>
    <!-- stars -->
    <polygon fill="var(--yellow)" points="1077,575 1086,598 1104,600 1090,613 1095,632 1077,621 1059,632 1064,613 1050,600 1068,598"/>
    <polygon fill="var(--star-red)" points="1031,574 1036,586 1047,587 1039,595 1042,606 1031,600 1020,606 1023,595 1015,587 1026,586"/>
    <polygon fill="var(--star-red)" points="1045,605 1048,612 1055,612 1050,617 1052,624 1045,620 1038,624 1040,617 1035,612 1042,612"/>
  </svg>

  <h1 class="title">Formative<br>Feedback<br>Teacher C/L or H/L</h1>
  <p class="label label--date">Date:</p>
  <span class="date-year">20</span>
  <p class="label label--strengths">Strengths (What Went Well…)</p>
  <p class="label label--red label--target">Target (Even Better if…)</p>
  <p class="label label--red label--action">action</p>
  <p class="label label--student">Response<br>(from the Student):</p>
  <p class="label label--teacher">Response and Reflection<br>(from the Teacher):</p>
</div>
</body>
</html>
```